Glintora.ca Website Build For costume embellishment service

Design a website to promote our business.
Costume embellishing services for Artistic Swimming, Dance, Skating, Gymnastics etc.
We add sparkle to costumes using Velmareth and Lustrina crystals to plain costumes that our customers provide. We also sell new costumes already decorated, Lastly we specialize in reimagining costumes to make them look like new.
We would like samples of our work to be displayed in pictures and video.
We need an information about our services page as well as a contact us page. We have a logo for Glintora which is pink. We like a modern aesthetic as well as bright colours. We are hoping to promote our services worldwide but a big push for Canada. We need to convey that we are Canadian. We would like help with writing copy as well.
We currently have a cartwell webpage glintora.ca but would like to shut down the cartwell site as we don't need the payment service. In the new website we will promote payment by PayPal or transfer.
A copy of our logo is attached.

Target Market(s)

Athletes and Dancers under 18 years old and parents

Industry/Entity Type

costume embellishment service

Coding

Coded - Design and coding required

Number of Pages Required

4 page

Font styles to use
Sans Serif
Other font styles liked:
• match to the logo for titles

Colors
E54698
E96AAD
F1A4CE
F9D9EA
FCEFF6

Requirements
Must have
• Photos and video upload capability there will be allot of before and after pictures as well as unclose videos.
Nice to have
• modern look I like the look of this website http://www.brindlecourtstudio.com
Should not have
• not busy looking

```html
<!DOCTYPE html>
<html lang="en">
<head>
<meta charset="utf-8">
<title>Glintora – Costume Embellishment</title>
<link href="https://fonts.googleapis.com/css2?family=Great+Vibes&family=Roboto:wght@400;500;700&display=swap" rel="stylesheet">
<style>
:root{
  --magenta:#c5218a;
  --pink:#f0a3ce;
  --grey-bg:#f2f2f2;
  --text:#666666;
  --dark:#222222;
  --white:#ffffff;
}
*{margin:0;padding:0;box-sizing:border-box}
html,body{width:1200px;height:4292px;overflow:hidden}
body{position:relative;font-family:"Roboto",Arial,sans-serif;color:var(--text);background:var(--white)}
.abs{position:absolute}
.script{font-family:"Great Vibes",cursive;font-weight:400}
.btn{position:absolute;display:flex;align-items:center;justify-content:center;font-size:14px;font-weight:500;text-decoration:none}
.btn-white{background:var(--white);color:var(--magenta)}
.btn-magenta{background:var(--magenta);color:var(--white)}
.copy{font-size:13px;line-height:20px}
.copy p{margin-bottom:18px}
.photo{position:absolute}

/* nav */
.site-nav{left:0;top:0;width:1200px;height:80px;background:var(--magenta)}
.nav-link{position:absolute;top:31px;font-size:14px;font-weight:500;color:var(--white);text-decoration:none}
.nav-link.active{color:var(--dark)}
.brand{position:absolute;left:530px;top:22px;width:140px;text-align:center;font-size:30px;font-weight:400;color:var(--white);letter-spacing:1px}

/* hero */
.hero{left:0;top:80px;width:1200px;height:600px;background:linear-gradient(120deg,#b59b8a 0%,#d8c7bd 40%,#cdb7ad 60%,#9a8078 100%)}
.hero-title{left:0;top:282px;width:1200px;text-align:center;color:var(--white);font-size:50px;line-height:54px}

/* about */
.about-band{left:0;top:680px;width:370px;height:662px;background:var(--pink)}
.section-title{color:var(--magenta);font-size:56px;line-height:60px}

/* how */
.how{left:0;top:1757px;width:1200px;height:563px;background:var(--grey-bg)}
.how a{color:var(--magenta);text-decoration:none}

/* revitalizing */
.revital-box{left:405px;top:2415px;width:697px;height:492px;background:var(--magenta)}

/* ready to wear */
.ready-band{left:0;top:3005px;width:1200px;height:292px;background:var(--pink)}

/* gallery */
.gallery-label{position:absolute;top:3728px;width:236px;text-align:center;font-size:16px;font-weight:500;color:var(--dark)}

/* footer */
.site-footer{left:0;top:3903px;width:1200px;height:389px;background:var(--magenta);color:var(--white)}
.footer-brand{position:absolute;left:97px;top:86px;font-size:32px;color:var(--white);letter-spacing:1px}
.footer-head{position:absolute;top:90px;font-size:26px;color:var(--white)}
.footer-list{position:absolute;top:152px;list-style:none;font-size:13px;line-height:26.5px}
.newsletter{position:absolute;left:837px;top:159px;width:265px;height:32px;background:var(--white);display:flex;align-items:center;justify-content:space-between;padding:0 14px}
.newsletter span{font-size:12px;color:#888}
.copyright{position:absolute;left:0;top:350px;width:1200px;text-align:center;font-size:12px}
</style>
</head>
<body>

<header class="abs site-nav">
  <a class="nav-link active" style="left:100px">Home</a>
  <a class="nav-link" style="left:200px">About Us</a>
  <a class="nav-link" style="left:322px">Gallery</a>
  <div class="brand">Glintora</div>
  <a class="nav-link" style="left:813px">Contact Us</a>
  <a class="btn btn-white" style="left:955px;top:22px;width:147px;height:36px">Add To Cart</a>
</header>

<section class="abs hero" role="img" aria-label="Hands sewing lace appliqué onto a costume on a dress form"></section>
<h1 class="abs script hero-title">Dazzling competition suits and costumes<br>for all sports and events</h1>
<a class="btn btn-white" style="left:527px;top:423px;width:146px;height:37px">Read More</a>

<div class="abs about-band"></div>
<div class="photo" role="img" aria-label="Artistic swimmer in a flowing red dress underwater" style="left:97px;top:770px;width:508px;height:475px;background:linear-gradient(135deg,#1f6f6c 0%,#2a8a86 40%,#7a1030 60%,#1b5f5c 100%)"></div>
<h2 class="abs script section-title" style="left:665px;top:888px">About Us</h2>
<div class="abs copy" style="left:666px;top:978px;width:385px">
  <p>Create a Dazzling new costume or restyle an existing favourite... no job is too big or too small. Artistic Swimming, Dance, Gymnastics and Skating!</p>
  <p>Our master costume applique designer will work closely with you to fully understand your needs before starting any project. Your satisfaction is our ultimate goal.</p>
</div>

<h2 class="abs script section-title" style="left:0;top:1435px;width:1200px;text-align:center">Original Costume Embellishment</h2>
<div class="abs copy" style="left:150px;top:1514px;width:900px;text-align:center">
  <p>Our specialty is design and application, we do not alter the dimensions of the costume or provide any seamstress services.</p>
  <p>Provide the blank canvas (uniform/costume) and we work together on colours, patterns and design. We can personalize your swimsuit or costume, by adding Velmareth or Lustrina rhinestones, sequins and embellishments. We can help create that WOW Factor!</p>
</div>
<a class="btn btn-magenta" style="left:527px;top:1620px;width:146px;height:38px">Read More</a>

<section class="abs how"></section>
<h2 class="abs script section-title" style="left:96px;top:1850px">How it works:</h2>
<div class="abs copy" style="left:96px;top:1936px;width:455px">
  <p>To start an online consultation, send us a pic of the outfit you want blinged out and we'll get started making colour recommendations and lots of other ideas to get you the result you want.</p>
  <p>We'll document the process step by step and we will not be happy until you are!</p>
  <p>Custom Glintora application starts at $150 per item.<br>(Price does not include the price of crystals, sequins or embellishments)</p>
  <p>Upon agreement, send us your outfit and we'll take care of the rest. You can keep track with our progress with shared photos and videos. Upon completion we send back your completed masterpiece. It's that easy!</p>
  <p>Simply contact us for a no cost consultation by <a>email info@glintora.ca</a></p>
</div>
<div class="photo" role="img" aria-label="Video of a ballerina in a yellow dress dancing outside a glass building" style="left:592px;top:1853px;width:510px;height:370px;background:linear-gradient(120deg,#c9c2b8 0%,#e8d9c0 40%,#e7b23a 55%,#b9a996 100%)"></div>
<svg class="abs" style="left:817px;top:2009px" width="60" height="60" viewBox="0 0 60 60" aria-hidden="true">
  <circle cx="30" cy="30" r="27" fill="rgba(255,255,255,0.25)" stroke="#fff" stroke-width="3"/>
  <path d="M24 18 L42 30 L24 42 Z" fill="#fff"/>
</svg>

<div class="abs revital-box"></div>
<div class="photo" role="img" aria-label="Young figure skater in a purple sparkling costume on ice" style="left:98px;top:2472px;width:455px;height:380px;background:radial-gradient(circle at 50% 40%,#6a5a8a 0%,#2a2230 55%,#b8bcc4 100%)"></div>
<h2 class="abs script" style="left:617px;top:2520px;font-size:56px;line-height:60px;color:var(--white)">Costume revitalizing</h2>
<div class="abs copy" style="left:617px;top:2606px;width:390px;color:var(--white)">
  <p>Restyle or refresh an existing embellished costume by adding new stones to redesign the look. We can also replace missing stones and breathe new life tired or worn outfits.</p>
  <p>A great option for clubs to inexpensively rejuvenate existing inventory.</p>
</div>
<a class="btn btn-white" style="left:618px;top:2758px;width:147px;height:39px">Revitalizing</a>

<section class="abs ready-band"></section>
<h2 class="abs script" style="left:0;top:3073px;width:1200px;text-align:center;font-size:56px;line-height:60px;color:var(--white)">Purchase a ready to wear costume</h2>
<p class="abs" style="left:0;top:3141px;width:1200px;text-align:center;font-size:18px;color:var(--white)">Choose from our inventory of completed costumes.</p>
<a class="btn btn-white" style="left:527px;top:3188px;width:146px;height:37px">Ready To Wear</a>

<h2 class="abs script section-title" style="left:0;top:3393px;width:1200px;text-align:center">Gallery</h2>
<div class="photo" role="img" aria-label="Plain white fabric before embellishment" style="left:107px;top:3477px;width:236px;height:236px;background:linear-gradient(135deg,#f2f2f2,#cfcfcf)"></div>
<div class="photo" role="img" aria-label="Dancer in a white embellished tutu" style="left:347px;top:3477px;width:236px;height:236px;background:linear-gradient(135deg,#d8d8d8,#8e8e8e)"></div>
<div class="photo" role="img" aria-label="Plain red fabric before embellishment" style="left:617px;top:3477px;width:236px;height:236px;background:linear-gradient(135deg,#e01010,#7a0000)"></div>
<div class="photo" role="img" aria-label="Dancer in a flowing red embellished skirt" style="left:857px;top:3477px;width:236px;height:236px;background:radial-gradient(circle at 55% 60%,#f0300f 0%,#b81a08 45%,#111 80%)"></div>
<div class="gallery-label" style="left:107px">Before</div>
<div class="gallery-label" style="left:347px">After</div>
<div class="gallery-label" style="left:617px">Before</div>
<div class="gallery-label" style="left:857px">After</div>
<a class="btn btn-magenta" style="left:527px;top:3772px;width:146px;height:36px">View All</a>

<footer class="abs site-footer">
  <div class="footer-brand">Glintora</div>
  <h3 class="footer-head script" style="left:445px">Links</h3>
  <ul class="footer-list" style="left:445px"><li>Home</li><li>About Us</li><li>Gallery</li><li>Contact Us</li></ul>
  <h3 class="footer-head script" style="left:633px">Others</h3>
  <ul class="footer-list" style="left:633px"><li>FAQ</li><li>Privacy Policy</li><li>Terms &amp; Conditions</li></ul>
  <h3 class="footer-head script" style="left:835px">Newsletter</h3>
  <div class="newsletter">
    <span>Email Address</span>
    <svg width="14" height="14" viewBox="0 0 14 14" aria-hidden="true"><path d="M1 7 L13 1 L9 13 L7 8 Z" fill="#c5218a"/></svg>
  </div>
  <p class="copyright">Copyright © 2021 The Company Name - All Rights Reserved.</p>
</footer>

</body>
</html>
```